Medical device engineering service firm needs an update to flier

We do engineering design work for medical products, from ideation through injection-molded prototypes. Our clients have assay that needs automation, or an idea that needs to be made concrete. We have a 2-sided flier that needs an update to the look. This flier is mainly used as both a take away at trade shows to describe our services and provide our contact information.

```html
<!DOCTYPE html>
<html lang="en">
<head>
<meta charset="utf-8">
<title>Veridant Product Development – Medical Device Development Process</title>
<link href="https://fonts.googleapis.com/css2?family=Roboto+Condensed:wght@300;400&family=Open+Sans:wght@700;800&family=Raleway:wght@400&display=swap" rel="stylesheet">
<style>
  :root{
    --purple:#7d2a7f;
    --purple-dark:#5e1a60;
    --green:#a7bd4f;
    --green-dark:#93a83f;
    --grey:#dadada;
    --ink:#1f1f1f;
    --white:#ffffff;
  }
  *{box-sizing:border-box;margin:0;padding:0}
  html,body{width:927px;height:1200px;overflow:hidden;background:var(--white)}
  .flier{position:relative;width:927px;height:1200px;overflow:hidden;background:var(--grey);font-family:"Roboto Condensed",Arial,sans-serif;color:var(--ink)}

  /* Header */
  .masthead{position:absolute;left:0;top:0;width:927px;height:210px}
  .masthead svg{position:absolute;left:0;top:0}
  .brand{position:absolute;left:38px;top:96px;color:var(--purple);font-family:"Roboto Condensed",Arial,sans-serif;font-weight:400;line-height:1}
  .brand-name{display:block;font-size:50px;letter-spacing:-1px}
  .brand-sub{display:block;font-size:14px;letter-spacing:.5px;margin-top:2px;padding-left:48px}
  .title{position:absolute;left:392px;top:30px;color:var(--white);font-weight:400;line-height:1}
  .title-kicker{display:block;font-size:35px;margin-bottom:12px}
  .title-main{display:block;font-size:49px;line-height:52px}

  /* Phase columns */
  .phase{position:absolute;top:238px;height:816px;background:var(--white)}
  .phase-1{left:27px;width:158px}
  .phase-2{left:211px;width:315px}
  .phase-3{left:558px;width:159px}
  .phase-4{left:747px;width:158px}
  .phase-head{position:relative;height:112px;color:var(--white);font-family:"Open Sans",Arial,sans-serif}
  .is-purple .phase-head{background:linear-gradient(120deg,var(--purple) 55%,#732677 55%)}
  .is-green .phase-head{background:linear-gradient(120deg,var(--green) 55%,#a0b64a 55%)}
  .phase-label{position:absolute;top:11px;font-size:17px;font-weight:700;letter-spacing:.3px}
  .phase-num{position:absolute;top:18px;font-size:84px;font-weight:800;letter-spacing:-2px;line-height:1.1}
  .phase-1 .phase-label,.phase-1 .phase-num,.phase-3 .phase-label,.phase-3 .phase-num,.phase-4 .phase-label,.phase-4 .phase-num{left:23px}
  .phase-2 .phase-label{left:155px}
  .phase-2 .phase-num{left:111px}
  .phase-num .amp{font-size:36px;letter-spacing:0}
  .pointer{position:absolute;bottom:-11px;width:0;height:0;border-left:11px solid transparent;border-right:11px solid transparent}
  .is-purple .pointer{border-top:11px solid var(--purple)}
  .is-green .pointer{border-top:11px solid var(--green)}

  .phase-body{display:flex;height:704px}
  .track{flex:1;display:flex;flex-direction:column}
  .phase-2 .track + .track{border-left:2px solid var(--green)}
  .step{position:relative;height:234px}
  .step:last-child{height:236px}
  .step::after{content:"";position:absolute;left:12px;right:12px;bottom:0;height:2px}
  .step:last-child::after{display:none}
  .is-purple .step::after{background:linear-gradient(90deg,transparent,rgba(125,42,127,.55),transparent)}
  .is-green .step::after{background:linear-gradient(90deg,transparent,rgba(167,189,79,.7),transparent)}
  .icon{position:absolute;left:50%;top:34px;width:64px;height:64px;transform:translateX(-50%)}
  .icon svg{width:64px;height:64px;display:block}
  .figure{border-radius:6px}
  .figure-green{background:linear-gradient(160deg,#c5d58a,#8fa23e)}
  .figure-desk{background:linear-gradient(180deg,#b8ca6e,#8c6a45)}
  .step-text{position:absolute;left:6px;right:6px;top:128px;height:84px;display:flex;align-items:center;justify-content:center;text-align:center;font-size:14.6px;line-height:18px;font-weight:400}

  /* Footer */
  .footer-rule{position:absolute;left:0;top:1085px;width:927px;height:5px;background:var(--green)}
  .footer{position:absolute;left:0;top:1090px;width:927px;height:110px;background:var(--white)}
  .address{position:absolute;left:64px;top:34px;font-family:"Raleway",Arial,sans-serif;font-size:21px;line-height:27px;letter-spacing:1.5px;color:#333}
  .footer-divider{position:absolute;left:359px;top:33px;width:2px;height:58px;background:#c9c9c9}
  .contact{position:absolute;left:399px;top:26px;font-family:"Raleway",Arial,sans-serif;font-size:26px;line-height:31px;letter-spacing:1.5px;color:#222}
  .cert{position:absolute;left:796px;top:24px;width:54px;height:54px;border-radius:50%;background:#2b3e8f}
</style>
</head>
<body>
<main class="flier">

  <header class="masthead">
    <svg width="927" height="210" viewBox="0 0 927 210" aria-hidden="true">
      <defs>
        <linearGradient id="mastGrey" x1="0" y1="0" x2="1" y2="0">
          <stop offset="0" stop-color="#ffffff"/>
          <stop offset="1" stop-color="#d8d8d8"/>
        </linearGradient>
      </defs>
      <rect width="927" height="210" fill="var(--purple)"/>
      <path d="M0 0 H330 Q342 110 312 210 H0 Z" fill="var(--green)"/>
      <path d="M0 0 H322 Q334 110 304 210 H0 Z" fill="url(#mastGrey)"/>
    </svg>
    <div class="brand">
      <span class="brand-name">veridant</span>
      <span class="brand-sub">PRODUCT DEVELOPMENT</span>
    </div>
    <h1 class="title">
      <span class="title-kicker">Steps To Success</span>
      <span class="title-main">Our Medical Device<br>Development Process</span>
    </h1>
  </header>

  <!-- Phase 01 -->
  <section class="phase phase-1 is-purple">
    <div class="phase-head">
      <span class="phase-label">PHASE</span>
      <span class="phase-num">01</span>
      <span class="pointer" style="left:106px"></span>
    </div>
    <div class="phase-body">
      <div class="track">
        <div class="step">
          <div class="icon"><svg viewBox="0 0 64 64" aria-hidden="true"><path d="M2 32 Q32 6 62 32 Q32 58 2 32 Z" fill="var(--purple-dark)"/><circle cx="32" cy="32" r="14" fill="#fff"/><circle cx="32" cy="32" r="10" fill="var(--purple-dark)"/><circle cx="27" cy="27" r="3" fill="#fff"/></svg></div>
          <p class="step-text">Discuss your project needs. Estimate the work to accomplish your vision.</p>
        </div>
        <div class="step">
          <div class="icon"><svg viewBox="0 0 64 64" aria-hidden="true"><g fill="none" stroke="var(--purple-dark)" stroke-width="4"><circle cx="28" cy="36" r="24"/><circle cx="28" cy="36" r="16"/><circle cx="28" cy="36" r="8"/></g><circle cx="28" cy="36" r="3" fill="var(--purple-dark)"/><path d="M28 36 L56 8" stroke="#444" stroke-width="3"/><path d="M52 4 L60 2 L58 10 L54 12 L50 8 Z" fill="#555"/></svg></div>
          <p class="step-text">Define the product requirements, giving us a well-defined target for development.</p>
        </div>
        <div class="step">
          <div class="icon"><svg viewBox="0 0 64 64" aria-hidden="true"><g stroke="var(--purple-dark)" stroke-width="3" stroke-linecap="round"><path d="M32 2 V8"/><path d="M12 10 L16 14"/><path d="M52 10 L48 14"/><path d="M4 28 H10"/><path d="M54 28 H60"/><path d="M10 46 L14 42"/><path d="M54 46 L50 42"/></g><circle cx="32" cy="30" r="15" fill="var(--purple-dark)"/><rect x="24" y="40" width="16" height="12" rx="2" fill="var(--purple-dark)"/><path d="M24 48 H40 M25 53 H39" stroke="#fff" stroke-width="2"/><rect x="28" y="56" width="8" height="4" rx="2" fill="var(--purple-dark)"/></svg></div>
          <p class="step-text">Brainstorm solutions, drawing from the experience of our entire engineering team.</p>
        </div>
      </div>
    </div>
  </section>

  <!-- Phase 02 -->
  <section class="phase phase-2 is-green">
    <div class="phase-head">
      <span class="phase-label">PHASE</span>
      <span class="phase-num">02</span>
      <span class="pointer" style="left:107px"></span>
      <span class="pointer" style="left:264px"></span>
    </div>
    <div class="phase-body">
      <div class="track">
        <div class="step">
          <div class="icon"><svg viewBox="0 0 64 64" aria-hidden="true"><rect x="26" y="4" width="12" height="5" rx="2" fill="var(--green)"/><rect x="27" y="10" width="10" height="4" fill="#555"/><rect x="27" y="15" width="10" height="4" fill="var(--green)"/><path d="M27 20 H37 V32 L48 58 H16 L27 32 Z" fill="#555"/><path d="M22 44 H42 L48 58 H16 Z" fill="var(--green)"/></svg></div>
          <p class="step-text">Develop concepts that provide an array of potential design solutions.</p>
        </div>
        <div class="step">
          <div class="icon figure figure-green" role="img" aria-label="Illustration of an engineer presenting concepts at a board"></div>
          <p class="step-text">Analyze and present concepts. Determine which one best meets all product requirements.</p>
        </div>
        <div class="step">
          <div class="icon figure figure-desk" role="img" aria-label="Illustration of an engineer designing at a desk"></div>
          <p class="step-text">Design all details in 3D CAD, defining tolerances, materials &amp; assembly methods.</p>
        </div>
      </div>
      <div class="track">
        <div class="step">
          <div class="icon"><svg viewBox="0 0 64 64" aria-hidden="true"><g fill="none" stroke="var(--green)" stroke-width="4" stroke-linecap="round"><path d="M6 50 H54"/><path d="M12 44 A20 20 0 1 1 46 24"/><path d="M40 8 A12 12 0 0 1 56 20"/></g><path d="M50 20 L60 18 L56 28 Z" fill="var(--green)"/><path d="M48 44 L58 50 L48 56 Z" fill="var(--green)"/></svg></div>
          <p class="step-text">Individually prototype any functions that are likely to require iteration.</p>
        </div>
        <div class="step">
          <div class="icon"><svg viewBox="0 0 64 64" aria-hidden="true"><path d="M10 28 A22 22 0 0 1 50 18 L56 12 V30 H38 L44 24 A14 14 0 0 0 18 28 Z" fill="var(--green-dark)"/><path d="M54 36 A22 22 0 0 1 14 46 L8 52 V34 H26 L20 40 A14 14 0 0 0 46 36 Z" fill="var(--green)"/></svg></div>
          <p class="step-text">Test prototypes against requirements. Quickly iterate with in-house prototyping.</p>
        </div>
        <div class="step">
          <div class="icon"><svg viewBox="0 0 64 64" aria-hidden="true"><rect x="8" y="8" width="38" height="50" rx="3" fill="var(--green)"/><rect x="12" y="14" width="30" height="40" fill="#fff"/><rect x="20" y="4" width="14" height="8" rx="2" fill="var(--green)"/><g stroke="var(--green)" stroke-width="2.5"><path d="M16 22 H20 M24 22 H38 M16 30 H20 M24 30 H38 M16 38 H20 M24 38 H34 M16 46 H20 M24 46 H30"/></g><circle cx="48" cy="48" r="12" fill="var(--green-dark)"/><path d="M42 48 L47 53 L55 43" fill="none" stroke="#fff" stroke-width="3"/></svg></div>
          <p class="step-text">Develop integrated prototype that combines all functions, and meets requirements.</p>
        </div>
      </div>
    </div>
  </section>

  <!-- Phase 03 -->
  <section class="phase phase-3 is-purple">
    <div class="phase-head">
      <span class="phase-label">PHASE</span>
      <span class="phase-num">03</span>
      <span class="pointer" style="left:108px"></span>
    </div>
    <div class="phase-body">
      <div class="track">
        <div class="step">
          <div class="icon"><svg viewBox="0 0 64 64" aria-hidden="true"><g fill="var(--purple-dark)"><rect x="27" y="4" width="10" height="58" rx="3" transform="rotate(-45 32 32)"/><rect x="27" y="4" width="10" height="58" rx="3" transform="rotate(45 32 32)"/><rect x="4" y="4" width="22" height="12" rx="2" transform="rotate(-45 15 10)"/><circle cx="52" cy="12" r="9"/></g><circle cx="55" cy="9" r="4" fill="#fff"/></svg></div>
          <p class="step-text">Fabricate prototype tooling in-house that we can easily iterate as needed.</p>
        </div>
        <div class="step">
          <div class="icon"><svg viewBox="0 0 64 64" aria-hidden="true"><g fill="none" stroke="var(--purple-dark)"><circle cx="24" cy="38" r="15" stroke-width="8" stroke-dasharray="6 5"/><circle cx="46" cy="16" r="10" stroke-width="6" stroke-dasharray="4.5 3.5"/></g><circle cx="24" cy="38" r="13" fill="var(--purple-dark)"/><circle cx="24" cy="38" r="5" fill="#fff"/><circle cx="46" cy="16" r="8" fill="var(--purple-dark)"/><circle cx="46" cy="16" r="3" fill="#fff"/></svg></div>
          <p class="step-text">Mold and assemble fully functional, production quality devices.</p>
        </div>
        <div class="step">
          <div class="icon"><svg viewBox="0 0 64 64" aria-hidden="true"><path d="M10 28 A22 22 0 0 1 50 18 L56 12 V30 H38 L44 24 A14 14 0 0 0 18 28 Z" fill="var(--purple-dark)"/><path d="M54 36 A22 22 0 0 1 14 46 L8 52 V34 H26 L20 40 A14 14 0 0 0 46 36 Z" fill="var(--purple-dark)"/></svg></div>
          <p class="step-text">Test molded devices against requirements. Iterate molds as needed.</p>
        </div>
      </div>
    </div>
  </section>

  <!-- Phase 4 & 5 -->
  <section class="phase phase-4 is-green">
    <div class="phase-head">
      <span class="phase-label">PHASE</span>
      <span class="phase-num">4<span class="amp">&amp;</span>5</span>
      <span class="pointer" style="left:107px"></span>
    </div>
    <div class="phase-body">
      <div class="track">
        <div class="step">
          <div class="icon"><svg viewBox="0 0 64 64" aria-hidden="true"><circle cx="26" cy="26" r="18" fill="none" stroke="var(--green)" stroke-width="6"/><path d="M39 39 L56 56" stroke="var(--green-dark)" stroke-width="9" stroke-linecap="round"/><path d="M16 26 L24 34 L44 12" fill="none" stroke="var(--green-dark)" stroke-width="5"/></svg></div>
          <p class="step-text">Perform Design Verification Testing to confirming that all designs requirements are met.</p>
        </div>
        <div class="step">
          <div class="icon"><svg viewBox="0 0 64 64" aria-hidden="true"><g fill="none" stroke="var(--green-dark)"><circle cx="16" cy="24" r="9" stroke-width="6" stroke-dasharray="4 3.2"/><circle cx="36" cy="10" r="6" stroke-width="5" stroke-dasharray="3 2.5"/></g><circle cx="16" cy="24" r="8" fill="var(--green-dark)"/><circle cx="16" cy="24" r="3" fill="#fff"/><circle cx="36" cy="10" r="5" fill="var(--green-dark)"/><rect x="28" y="24" width="28" height="36" rx="3" fill="var(--green)"/><rect x="31" y="29" width="22" height="28" fill="#fff"/><rect x="36" y="21" width="12" height="6" rx="2" fill="var(--green)"/><path d="M34 35 H50 M34 41 H50 M34 47 H50 M34 53 H46" stroke="var(--green)" stroke-width="2.5"/></svg></div>
          <p class="step-text">Seamlessly transfer to manufacturing for production scale up.</p>
        </div>
        <div class="step">
          <div class="icon"><svg viewBox="0 0 64 64" aria-hidden="true"><rect x="4" y="4" width="34" height="44" rx="3" fill="var(--green)"/><rect x="10" y="10" width="34" height="44" rx="3" fill="var(--green-dark)"/><rect x="16" y="16" width="34" height="44" rx="3" fill="var(--green)"/><rect x="20" y="20" width="26" height="36" fill="#fff"/><path d="M26 36 L34 46 L60 18" fill="none" stroke="var(--green)" stroke-width="5"/></svg></div>
          <p class="step-text">Support patent and regulatory approval processes.</p>
        </div>
      </div>
    </div>
  </section>

  <div class="footer-rule"></div>
  <footer class="footer">
    <p class="address">2240 Alder Ridge Way<br>Vista, CA 92083</p>
    <div class="footer-divider"></div>
    <p class="contact">VeridantPD.com<br>+1 760 555 0148</p>
    <div class="cert" role="img" aria-label="Quality certification badge"></div>
  </footer>

</main>
</body>
</html>
```